Property Developer Business card design

we need a business card design + printing for a new Property developer company based in melbourne.
We are a group of investors investing in a property developer business. We have more projects involved in residential property as opposed to commercial property but we are involved in both market. we also provide consulting services with overseas investors willing to invest in the australian property market.
Updates
I have uploaded the logo. I'm not very convince with the colors of my logo... any suggestion please?.
Thanks guys!
Target Market(s)
property investors or person willing to purchase investment property
Industry/Entity Type
Residential
Contact Information for Business Card
Tallgrove Holdings Australia Pty Ltd
Look and feel
Each slider illustrates characteristics of the customer's brand and the style your logo design should communicate.

```html
<!DOCTYPE html>
<html lang="en">
<head>
<meta charset="utf-8">
<title>Tallgrove Holdings – Business Card</title>
<link rel="stylesheet" href="https://fonts.googleapis.com/css2?family=Ubuntu:wght@400;500;700&display=swap">
<style>
  :root {
    --bg: #e9e9ea;
    --card-top: #ffffff;
    --card-bottom: #e6e6e6;
    --ink: #2b2b2b;
    --red: #c3202b;
    --grey: #9a9a9a;
    --faint: #d9d9d9;
  }
  * { box-sizing: border-box; margin: 0; padding: 0; }
  html, body { width: 1200px; height: 900px; overflow: hidden; }
  body {
    background: var(--bg);
    font-family: "Ubuntu", sans-serif;
    color: var(--ink);
    position: relative;
  }
  .card {
    position: absolute;
    width: 620px;
    height: 350px;
    border-radius: 18px;
    background: linear-gradient(160deg, var(--card-top) 0%, var(--card-bottom) 100%);
    box-shadow: 0 10px 28px rgba(0,0,0,0.18);
    overflow: hidden;
  }
  .card--back { left: 80px; top: 90px; }
  .card--front { left: 500px; top: 460px; }

  .brand {
    display: flex;
    align-items: center;
    gap: 10px;
  }
  .brand__square {
    width: 22px; height: 22px;
    background: var(--red);
  }
  .brand__name {
    font-weight: 700;
    font-size: 28px;
    color: var(--ink);
    line-height: 1;
  }

  /* back */
  .card--back .brand { position: absolute; left: 48px; top: 220px; }
  .back__mark {
    position: absolute;
    left: 300px; top: -40px;
    width: 320px; height: 320px;
    border-radius: 50%;
    background: radial-gradient(circle, var(--faint) 0%, rgba(217,217,217,0) 70%);
  }
  .back__legal {
    position: absolute;
    right: 40px; top: 170px;
    text-align: right;
  }
  .back__company { color: var(--red); font-weight: 700; font-size: 17px; }
  .back__abn { font-weight: 700; font-size: 14px; margin-top: 6px; }

  /* front */
  .card--front .brand { position: absolute; left: 40px; top: 138px; }
  .front__divider {
    position: absolute;
    left: 342px; top: 58px;
    width: 2px; height: 120px;
    background: var(--ink);
  }
  .person { position: absolute; left: 372px; top: 52px; }
  .person__name { font-weight: 700; font-size: 20px; }
  .person__role { color: var(--red); font-size: 12px; margin-top: 3px; }
  .contacts { list-style: none; position: absolute; left: 372px; top: 110px; }
  .contacts li {
    display: flex; align-items: center; gap: 10px;
    font-weight: 500; font-size: 13px; line-height: 21px;
  }
  .contacts .icon { width: 12px; height: 12px; flex: none; }
  .contacts .spacer { width: 12px; flex: none; }
  .location {
    position: absolute; left: 0; right: 0; top: 250px;
    text-align: center;
    font-weight: 700; font-size: 16px;
  }
  .location p { display: flex; justify-content: center; align-items: center; gap: 8px; line-height: 30px; }
  .location svg { width: 15px; height: 15px; }
</style>
</head>
<body>

<section class="card card--back" aria-label="Card back">
  <div class="back__mark" role="img" aria-label="Faint brand mark decoration"></div>
  <div class="brand">
    <span class="brand__square"></span>
    <span class="brand__name">Tallgrove Holdings</span>
  </div>
  <div class="back__legal">
    <p class="back__company">Tallgrove Holdings Australia Pty Ltd</p>
    <p class="back__abn">ABN : 00 482 917 365</p>
  </div>
</section>

<section class="card card--front" aria-label="Card front">
  <div class="brand">
    <span class="brand__square"></span>
    <span class="brand__name">Tallgrove Holdings</span>
  </div>
  <div class="front__divider"></div>
  <div class="person">
    <p class="person__name">Daniel Reyes</p>
    <p class="person__role">Managing Director</p>
  </div>
  <ul class="contacts">
    <li>
      <svg class="icon" viewBox="0 0 24 24"><path fill="#c3202b" d="M6.6 10.8a15 15 0 0 0 6.6 6.6l2.2-2.2c.3-.3.7-.4 1-.2 1.1.4 2.3.6 3.6.6.6 0 1 .4 1 1V20c0 .6-.4 1-1 1A17 17 0 0 1 3 4c0-.6.4-1 1-1h3.5c.6 0 1 .4 1 1 0 1.3.2 2.5.6 3.6.1.3 0 .7-.2 1z"/></svg>
      +61 3 9000 4821
    </li>
    <li>
      <svg class="icon" viewBox="0 0 24 24"><rect x="6" y="2" width="12" height="20" rx="2" fill="none" stroke="#c3202b" stroke-width="2.4"/><circle cx="12" cy="18" r="1.3" fill="#c3202b"/></svg>
      0400 552 318
    </li>
    <li>
      <svg class="icon" viewBox="0 0 24 24"><circle cx="12" cy="12" r="4" fill="none" stroke="#c3202b" stroke-width="2.4"/><path d="M16 8v5a3 3 0 0 0 6 0v-1a10 10 0 1 0-4 8" fill="none" stroke="#c3202b" stroke-width="2.4"/></svg>
      daniel.reyes@tallgrove.com.au
    </li>
    <li><span class="spacer"></span>directors@tallgrove.com.au</li>
    <li><span class="spacer"></span>members@tallgrove.com.au</li>
  </ul>
  <div class="location">
    <p>
      <svg viewBox="0 0 24 24"><path fill="#c3202b" d="M12 3 2 12h3v8h5v-5h4v5h5v-8h3z"/></svg>
      www.tallgrove.com.au
    </p>
    <p>
      <svg viewBox="0 0 24 24"><path fill="#c3202b" d="M12 2a7 7 0 0 0-7 7c0 5 7 13 7 13s7-8 7-13a7 7 0 0 0-7-7zm0 9.5A2.5 2.5 0 1 1 12 6.5a2.5 2.5 0 0 1 0 5z"/></svg>
      12 Wattlebird Lane Sunvale VIC 3999, Australia
    </p>
  </div>
</section>

</body>
</html>
```